Statistics Dashboard

I need a statistics dashboard for one of our projects.
Just a simple single page to showcase the various stats in a beautiful way.
Angular is the framework of choice. (Not Angular.js)
The app will call an API to get the following information:
1- Number of current users
2- Number of users on Nimbus
3- Number of users on Vela
4- Number of newly registered users this week
5- All time service requests
6- Service requests this week
7- Number of subscribers for each telecom company (2-3 companies).

```html
<!DOCTYPE html>
<html lang="en">
<head>
<meta charset="utf-8">
<title>My Dashboard</title>
<link rel="stylesheet" href="https://fonts.googleapis.com/css2?family=Lato:wght@400;700&display=swap">
<style>
  :root {
    --navy: #263d5e;
    --page: #e1e2e5;
    --panel: #ebebed;
    --ink: #3a3d44;
    --muted: #4a4f58;
    --rule: #c9cbd0;
    --red: #ff5a55;
    --red-text: #f2564f;
    --green: #14c466;
    --green-text: #1fbd62;
    --white: #ffffff;
    --avatar: #d9d9da;
    --company-1: #d62a4c;
    --company-2: #a54ed4;
    --company-3: #3552d1;
  }
  * { box-sizing: border-box; margin: 0; padding: 0; }
  html, body { width: 1200px; height: 581px; overflow: hidden; }
  body {
    position: relative;
    background: var(--page);
    font-family: "Lato", sans-serif;
    color: var(--ink);
  }
  .topbar {
    position: absolute; left: 0; top: 0; width: 1200px; height: 115px;
    background: var(--navy);
    display: flex; align-items: center; justify-content: center;
  }
  .topbar h1 { color: var(--white); font-size: 27px; font-weight: 700; letter-spacing: 0.3px; }

  .panel { position: absolute; background: var(--panel); }
  .panel-title {
    position: absolute; left: 36px; top: 28px;
    font-size: 17.5px; font-weight: 400; color: var(--muted); letter-spacing: 0.4px;
  }

  .users { left: 45px; top: 155px; width: 734px; height: 248px; }
  .user-stats { position: absolute; left: 36px; top: 70px; width: 424px; list-style: none; }
  .user-stats li {
    display: flex; justify-content: space-between; align-items: baseline;
    font-size: 29px; line-height: 41.5px;
  }
  .user-stats .value { font-weight: 700; }
  .user-stats .platform-a { color: var(--red-text); }
  .user-stats .platform-b { color: var(--green-text); }

  .share-chart { position: absolute; left: 497px; top: 59px; width: 214px; height: 167px; }
  .bar { position: absolute; bottom: 0; color: var(--white); text-align: center; }
  .bar .pct { display: block; font-size: 28px; margin-top: 14px; }
  .bar .label { position: absolute; left: 0; right: 0; bottom: 8px; font-size: 18px; }
  .bar-a { left: 0; width: 104px; height: 167px; background: var(--red); }
  .bar-b { left: 104px; width: 110px; height: 135px; background: var(--green); }

  .requests { left: 805px; top: 155px; width: 355px; height: 248px; }
  .requests .panel-title { left: 34px; }
  .request-row {
    position: absolute; left: 34px; width: 277px;
    display: flex; justify-content: space-between; align-items: center;
    font-size: 29px;
  }
  .request-row .label { padding-top: 18px; }
  .request-row.all-time { top: 75px; }
  .request-row.this-week { top: 157px; }
  .request-divider { position: absolute; left: 34px; top: 144px; width: 277px; height: 1px; background: var(--rule); }
  .badge { color: var(--white); font-size: 33px; line-height: 56px; height: 56px; padding: 0 10px; border-radius: 3px; }
  .badge-red { background: var(--red); }
  .badge-green { background: var(--green); min-width: 57px; text-align: center; }

  .company { top: 434px; width: 355px; height: 111px; }
  .company-1 { left: 45px; }
  .company-2 { left: 424px; width: 356px; }
  .company-3 { left: 805px; }
  .company .avatar { position: absolute; left: 15px; top: 25px; }
  .company .name { position: absolute; left: 86px; top: 25px; font-size: 17.5px; font-weight: 400; letter-spacing: 0.3px; }
  .company-1 .name { color: var(--company-1); }
  .company-2 .name { color: var(--company-2); }
  .company-3 .name { color: var(--company-3); }
  .company .count { position: absolute; left: 86px; top: 46px; white-space: nowrap; }
  .company .count strong { font-size: 36px; font-weight: 700; color: var(--ink); }
  .company .count span { font-size: 19px; margin-left: 10px; color: var(--muted); }
</style>
</head>
<body>
  <header class="topbar"><h1>MY DASHBOARD</h1></header>

  <section class="panel users">
    <h2 class="panel-title">NUMBER OF USERS</h2>
    <ul class="user-stats">
      <li><span>Current Users</span><span class="value">40,045</span></li>
      <li><span>New Users This Week</span><span class="value">8,045</span></li>
      <li class="platform-a"><span>Nimbus Users</span><span class="value">14,045</span></li>
      <li class="platform-b"><span>Vela Users</span><span class="value">12,005</span></li>
    </ul>
    <div class="share-chart">
      <div class="bar bar-a"><span class="pct">58%</span><span class="label">Nimbus</span></div>
      <div class="bar bar-b"><span class="pct">42%</span><span class="label">Vela</span></div>
    </div>
  </section>

  <section class="panel requests">
    <h2 class="panel-title">SERVICE REQUESTS</h2>
    <div class="request-row all-time"><span class="label">All Time</span><span class="badge badge-red">2,912</span></div>
    <div class="request-divider"></div>
    <div class="request-row this-week"><span class="label">This Week</span><span class="badge badge-green">25</span></div>
  </section>

  <section class="panel company company-1">
    <svg class="avatar" width="60" height="60" viewBox="0 0 60 60"><circle cx="30" cy="30" r="30" fill="var(--avatar)"/></svg>
    <h3 class="name">COMPANY 1</h3>
    <p class="count"><strong>5,100</strong><span>subscribers</span></p>
  </section>

  <section class="panel company company-2">
    <svg class="avatar" width="60" height="60" viewBox="0 0 60 60"><circle cx="30" cy="30" r="30" fill="var(--avatar)"/></svg>
    <h3 class="name">COMPANY 2</h3>
    <p class="count"><strong>9,180</strong><span>subscribers</span></p>
  </section>

  <section class="panel company company-3">
    <svg class="avatar" width="60" height="60" viewBox="0 0 60 60"><circle cx="30" cy="30" r="30" fill="var(--avatar)"/></svg>
    <h3 class="name">COMPANY 3</h3>
    <p class="count"><strong>91,230</strong><span>subscribers</span></p>
  </section>
</body>
</html>
```